Copperleaf Grill
there is none
Copperleaf Grill -
Simple
Danielle Whitcomb
Proprietor
318 Ferrand Street New Orleans, LA 70119
dwhitcomb@copperleaf-eats.com
www.copperleaf-eats.com
Use the same font of Grill and New Orleans for information on card
Just put the logo and website on the back of the card

```html
<!DOCTYPE html>
<html lang="en">
<head>
<meta charset="utf-8">
<title>Copperleaf Grill – Business Cards</title>
<link rel="stylesheet" href="https://fonts.googleapis.com/css2?family=Source+Sans+3:wght@400;600&display=swap">
<style>
  :root {
    --paper: #ffffff;
    --frame: #9a9a9a;
    --maroon: #7b1c2c;
    --maroon-dark: #5e1220;
    --silver-light: #f2f2f2;
    --silver-mid: #d6d6d6;
    --silver-dark: #b5b5b5;
    --ink: #2b2b2b;
    --white: #ffffff;
  }
  * { box-sizing: border-box; margin: 0; padding: 0; }
  html, body { width: 1200px; height: 780px; overflow: hidden; background: var(--paper); }
  .canvas {
    position: relative;
    width: 1200px; height: 780px;
    background: var(--paper);
    font-family: "Source Sans 3", Arial, sans-serif;
  }
  .presentation-frame {
    position: absolute; left: 6px; top: 6px; right: 6px; bottom: 6px;
    border: 2px solid var(--frame);
  }
  .card {
    position: absolute;
    width: 418px; height: 234px;
    border-radius: 16px;
    border: 2px solid #3a3a3a;
    overflow: hidden;
    box-shadow: 0 2px 4px rgba(0,0,0,0.2);
  }
  .card--front { left: 173px; top: 139px; background: var(--maroon); }
  .card--back-silver {
    left: 614px; top: 139px;
    background: radial-gradient(ellipse at 50% 45%, var(--silver-light) 0%, var(--silver-mid) 60%, var(--silver-dark) 100%);
  }
  .card--back-maroon { left: 380px; top: 404px; background: var(--maroon); }

  .silver-band {
    position: absolute; left: 0; right: 0; top: 72px; height: 103px;
    background: linear-gradient(90deg, var(--silver-dark) 0%, var(--silver-light) 30%, var(--silver-light) 70%, var(--silver-dark) 100%);
  }
  .holder {
    position: absolute; right: 24px; top: 20px;
    color: var(--white); text-align: left;
  }
  .holder-name { font-size: 17px; font-weight: 400; line-height: 1.1; }
  .holder-title { font-size: 12px; line-height: 1.2; }

  .wordmark {
    position: absolute; left: 0; right: 0;
    display: flex; align-items: center; justify-content: center; gap: 10px;
    font-size: 34px; font-weight: 600; letter-spacing: 0.5px;
  }
  .wordmark-dot { width: 16px; height: 16px; border-radius: 50%; }
  .card--front .wordmark { top: 100px; color: var(--ink); }
  .card--front .wordmark-dot { background: var(--maroon); }
  .card--back-silver .wordmark { top: 86px; color: var(--ink); }
  .card--back-silver .wordmark-dot { background: var(--maroon); }
  .card--back-maroon .wordmark { top: 86px; color: var(--white); }
  .card--back-maroon .wordmark-dot { background: var(--white); }

  .contact {
    position: absolute; left: 0; right: 0; bottom: 14px;
    color: var(--white); text-align: center;
    font-size: 10.5px; line-height: 1.45;
  }
  .website {
    position: absolute; left: 0; right: 0; bottom: 20px;
    text-align: center; font-size: 15px;
  }
  .card--back-silver .website { color: var(--ink); }
  .card--back-maroon .website { color: var(--white); }
</style>
</head>
<body>
<main class="canvas">
  <div class="presentation-frame"></div>

  <section class="card card--front" aria-label="Card front">
    <div class="silver-band"></div>
    <div class="holder">
      <p class="holder-name">Danielle Whitcomb</p>
      <p class="holder-title">Proprietor</p>
    </div>
    <div class="wordmark"><span class="wordmark-dot"></span><span>Copperleaf Grill</span></div>
    <div class="contact">
      <p>318 Ferrand Street New Orleans, LA 70119 &nbsp;Phone 504.555.0142</p>
      <p>Cell 225.555.0187 &nbsp;Email dwhitcomb@copperleaf-eats.com</p>
    </div>
  </section>

  <section class="card card--back-silver" aria-label="Card back, silver">
    <div class="wordmark"><span class="wordmark-dot"></span><span>Copperleaf Grill</span></div>
    <p class="website">www.copperleaf-eats.com</p>
  </section>

  <section class="card card--back-maroon" aria-label="Card back, maroon">
    <div class="wordmark"><span class="wordmark-dot"></span><span>Copperleaf Grill</span></div>
    <p class="website">www.copperleaf-eats.com</p>
  </section>
</main>
</body>
</html>
```